Professional Business Card for Commercial Cleaning Company

We need a business card that represents our commercial janitorial cleaning company and represent several brands for our company so we do not want to highlight the logo too much. We want something that says we are professional.
Notes:No website or address as we have many locations and many websites and companies under our corporate name of "Brightvale Holdings, LLC" . Every time we hand a customer a business card they have contacted us via another brand we own but we don't want to have 21 business cards so we want to not focus on Brightvale Holdings, LLC too much since people will automatically ask "What is Brightvale Holdings, LLC" Example: Noodle Barn and Wrap Lantern restaurants are owned by "Zest! Brands" is the corporation name. Same principle here. Except we do not advertise at this time that all of our brands are connected. Hope this helps.
Target Market(s)
Commercial Cleaning
Industry/Entity Type
Janitorial Service
Contact Information for Business Card
Milo Jarvis
Business Development
555-382-9047
sales@brightvaleholdingsllc.example
Requirements
Must have
- Logo with contact information, need to be able to easily edit contact info for others in my office.
Nice to have
- Professional Image. Like to see a colorful bold look and a more standard business card look.
Should not have
- Any type of cleaning icons, tools, people or water.

```html
<!DOCTYPE html>
<html lang="en">
<head>
<meta charset="utf-8">
<title>Brightvale Holdings, LLC — Business Card</title>
<link rel="stylesheet" href="https://fonts.googleapis.com/css2?family=Questrial&family=Open+Sans:wght@400&display=swap">
<style>
  :root {
    --navy: #1c3b78;
    --green: #5fa63a;
    --ink: #2a2a2a;
    --paper: #ffffff;
    --backdrop: #d8d8d8;
  }
  * { margin: 0; padding: 0; box-sizing: border-box; }
  html, body { width: 1200px; height: 872px; overflow: hidden; }
  body {
    background: var(--backdrop);
    display: flex;
    align-items: center;
    justify-content: center;
    gap: 48px;
    font-family: "Open Sans", sans-serif;
  }
  .card {
    position: relative;
    width: 540px;
    height: 309px;
    background: var(--paper);
    box-shadow: 0 6px 18px rgba(0,0,0,0.18);
    overflow: hidden;
  }
  .card-band {
    position: absolute;
    inset: 0;
    width: 100%;
    height: 100%;
  }
  .wordmark {
    font-family: "Questrial", sans-serif;
    color: var(--navy);
    white-space: nowrap;
  }
  .card-front .wordmark {
    position: absolute;
    right: 36px;
    top: 150px;
    font-size: 29px;
  }
  .contact {
    position: absolute;
    right: 36px;
    top: 204px;
    text-align: right;
  }
  .contact-name {
    font-family: "Questrial", sans-serif;
    font-size: 19px;
    letter-spacing: 0.5px;
    color: var(--navy);
    text-transform: uppercase;
  }
  .contact-title {
    font-size: 11px;
    color: var(--ink);
    margin-bottom: 10px;
  }
  .contact-line {
    font-size: 12px;
    color: var(--ink);
    display: flex;
    align-items: center;
    justify-content: flex-end;
    gap: 6px;
    line-height: 1.55;
  }
  .contact-icon { width: 10px; height: 10px; fill: var(--green); }
  .card-back {
    display: flex;
    align-items: center;
    justify-content: center;
  }
  .card-back .wordmark { font-size: 34px; }
</style>
</head>
<body>
  <section class="card card-front">
    <svg class="card-band" viewBox="0 0 540 309" preserveAspectRatio="none" aria-hidden="true">
      <path d="M150,0 L540,0 L540,150 Q360,30 150,0 Z" fill="var(--navy)"/>
      <path d="M40,58 Q330,0 540,168" fill="none" stroke="var(--paper)" stroke-width="10"/>
      <path d="M60,70 Q330,20 540,178" fill="none" stroke="var(--green)" stroke-width="4"/>
    </svg>
    <div class="wordmark">Brightvale Holdings, LLC</div>
    <div class="contact">
      <div class="contact-name">Milo Jarvis</div>
      <div class="contact-title">Business Development</div>
      <div class="contact-line">
        <svg class="contact-icon" viewBox="0 0 10 10" aria-hidden="true"><path d="M2,0 L4,2.5 L3,3.6 Q4.2,5.8 6.4,7 L7.5,6 L10,8 L8.6,10 Q3,9 0,1.4 Z"/></svg>
        <span>555-382-9047</span>
      </div>
      <div class="contact-line">
        <svg class="contact-icon" viewBox="0 0 10 10" aria-hidden="true"><path d="M0,2 L10,2 L10,8 L0,8 Z M0,2 L5,5.5 L10,2" /></svg>
        <span>sales@brightvaleholdingsllc.example</span>
      </div>
    </div>
  </section>

  <section class="card card-back">
    <div class="wordmark">Brightvale Holdings, LLC</div>
  </section>
</body>
</html>
```